Business Cards for new orthopaedic surgery practice

My husband and I are starting our own orthopaedic surgery practice. We are looking for a business card that is uniform, but one will have my name/title and the other will have his. You can just create one design with my name on it for now. But when I choose your design as the winning design I will ask that you add another copy with his name/title.

We are looking for classy, simple, elite all in one. We like dark blues/a little gold/yellow. Something that goes with our logo. We want our logo incorporated. Here is all the info you need:
Business name: RV Spine & Vitality Center
Location: 38915 North Bramble Ave
Maple Hollow, FL 33980
Phone: 954-218-4630
Fax: 954-571-2846
Email: info@myrvspine.example

Names: Lucinda Ferrow, M.D.
Board Certified Hand and Upper Extremity Surgeon

Emeka Dlunga, M.D.
Board Certified Hip & Knee Replacement/General Orthopaedic Surgeon

Can decide what you want to put on the back. Maybe a slogan:
Grounded in Skill. Devoted to You

I am just going to upload our logo. The only thing is if we select you as the winning design, the location, and phone numbers may change. We will need your help to update that once fully solidified.

Industry/Entity Type

Medical

Contact Information for Business Card

Colors
0054AA
0677BA
7BADD7
CADEEF
E8F1F8
0094D4
00A9DD
6FCCEA
C7EBF8
E9F6FB

Requirements
Must have
• class, appeal,
Should not have
• We want to air on the side of masculine if we are looking at masculine vs. feminine feel. But we still want it classy, sophisticated, and something we will love

```html
<!DOCTYPE html>
<html lang="en">
<head>
<meta charset="utf-8">
<title>RV Spine &amp; Vitality Center — Business Card</title>
<link rel="stylesheet" href="https://fonts.googleapis.com/css2?family=EB+Garamond:wght@400;600;700&display=swap">
<style>
  :root {
    --navy: #0e1a44;
    --navy-soft: #1d2b5e;
    --gold: #c9a04a;
    --paper: #f6f6f4;
    --stage: #e7e4dd;
    --grey: #4d5168;
    --band-text: #e9ecf5;
    --rule: rgba(233, 236, 245, 0.45);
  }
  * { margin: 0; padding: 0; box-sizing: border-box; }
  html, body { width: 1200px; height: 900px; overflow: hidden; }
  body {
    background: var(--stage);
    font-family: "EB Garamond", Georgia, serif;
    position: relative;
  }
  .card {
    position: absolute;
    left: 280px;
    width: 640px;
    height: 366px;
    background: var(--paper);
    overflow: hidden;
    box-shadow: 0 6px 18px rgba(14, 26, 68, 0.18);
  }
  .card--front { top: 70px; }
  .card--back { top: 470px; }

  .band {
    position: absolute;
    left: 0; right: 0; bottom: 0;
    height: 110px;
    background: var(--navy);
  }
  .illustration {
    position: absolute;
    left: 0; bottom: 0;
    width: 232px;
    height: 256px;
    background: linear-gradient(180deg, var(--navy-soft) 0%, var(--navy) 100%);
    border-top-right-radius: 90px;
  }

  .brand {
    position: absolute;
    top: 34px;
    right: 36px;
    display: flex;
    align-items: center;
    gap: 12px;
    color: var(--navy);
  }
  .brand__dot {
    width: 16px; height: 16px;
    border-radius: 50%;
    background: var(--gold);
    flex: none;
  }
  .brand__name {
    font-size: 21px;
    font-weight: 600;
    line-height: 1.1;
    letter-spacing: 0.02em;
  }

  .identity {
    position: absolute;
    left: 252px;
    top: 176px;
    color: var(--navy);
  }
  .identity__name {
    font-size: 22px;
    font-weight: 700;
    letter-spacing: 0.02em;
    text-transform: uppercase;
  }
  .identity__title {
    font-size: 15.5px;
    color: var(--grey);
    margin-top: 2px;
  }

  .contact {
    position: absolute;
    left: 252px;
    top: 272px;
    display: flex;
    color: var(--band-text);
    font-size: 15px;
    line-height: 1.45;
  }
  .contact__list { list-style: none; padding-right: 18px; }
  .contact__list li { display: flex; align-items: center; gap: 8px; }
  .contact__icon { width: 12px; height: 12px; flex: none; }
  .contact__address {
    font-style: normal;
    border-left: 1px solid var(--rule);
    padding-left: 16px;
    align-self: center;
  }

  .slogan {
    position: absolute;
    right: 40px;
    bottom: 40px;
    color: var(--gold);
    font-size: 24px;
    font-weight: 600;
    letter-spacing: 0.01em;
  }
</style>
</head>
<body>

  <section class="card card--front" aria-label="Business card front">
    <div class="band"></div>
    <div class="illustration" role="img" aria-label="Navy silhouette illustration of a large tree with a seated figure beneath it"></div>

    <div class="brand">
      <span class="brand__dot"></span>
      <span class="brand__name">RV Spine &amp;<br>Vitality Center</span>
    </div>

    <div class="identity">
      <p class="identity__name">Lucinda Ferrow, M.D.</p>
      <p class="identity__title">Board Certified Hand and Upper Extremity Surgeon</p>
    </div>

    <div class="contact">
      <ul class="contact__list">
        <li>
          <svg class="contact__icon" viewBox="0 0 12 12" aria-hidden="true"><path fill="#c9a04a" d="M2.4 0.6 L4.2 2.6 L3.2 3.8 Q4.4 6.6 7.8 8.6 L9 7.6 L11.2 9.4 L10 11.2 Q4.6 11 0.8 2 Z"/></svg>
          954-218-4630
        </li>
        <li>
          <svg class="contact__icon" viewBox="0 0 12 12" aria-hidden="true"><rect x="3" y="0.5" width="6" height="3.5" fill="#c9a04a"/><rect x="0.5" y="4.5" width="11" height="5" rx="1" fill="#c9a04a"/><rect x="3" y="8" width="6" height="3.5" fill="#c9a04a" stroke="#0e1a44" stroke-width="0.8"/></svg>
          954-571-2846
        </li>
        <li>
          <svg class="contact__icon" viewBox="0 0 12 12" aria-hidden="true"><rect x="0.5" y="2" width="11" height="8" fill="#c9a04a"/><path d="M0.5 2 L6 7 L11.5 2" fill="none" stroke="#0e1a44" stroke-width="1"/></svg>
          info@myrvspine.example
        </li>
      </ul>
      <address class="contact__address">
        38915 North Bramble Ave<br>Maple Hollow, FL 33980
      </address>
    </div>
  </section>

  <section class="card card--back" aria-label="Business card back">
    <div class="band"></div>
    <div class="illustration" role="img" aria-label="Navy silhouette illustration of a large tree with a seated figure beneath it"></div>

    <div class="brand">
      <span class="brand__dot"></span>
      <span class="brand__name">RV Spine &amp;<br>Vitality Center</span>
    </div>

    <p class="slogan">Grounded in Skill. Devoted to You</p>
  </section>

</body>
</html>
```